WordPress WEB DESIGN & CODING for www.quellbrook-rigging.com Wireless Tower Contruction

WEB DESIGN & CODING for www.quellbrook-rigging.com
Wireless Tower Contruction Industry

SLOGAN: SERVICE AT A HIGHER LEVEL

Pardune Masts LLC has been in business since 2014 with combined professional Team experience of over 40 years.

Our Team is composed of long-time industry professionals in every aspect of the wireless telecommunications and commercial construction industries, including project management and site acquisition.

Pardune Masts specializes in providing tower installation services for the Wireless Telecommunications in the Southeastern of the United States.

Our key services are Wireless Tower Construction, Installation & Maintenance

Site audits and Tower mapping
Mount swaps and Modifications
Hardline & Jumper Installation
Antenna & Radio Install, Decom, Testing and Maintenance
Tower Lighting Installation & Testing
Fiber / Sweep / RET/ PIM Testing
Small Cells
Civil installation (concrete/steel platforms/electrical)
____________________________________________________________________

we need a clean yet vibrant, energetic website design that will convey our tower installation work to the fullest... It should use the navy and green colors of our logo and it must be mobile friendly and coded for both Android & IOS;
the site structure:
HOME
ABOUT
SERVICES
CONTRACT
CAREERS
GALLERY

I also attach a few pics we bought on pixgranary so these can be used if needed as we own them...

Target Market(s)

Client: large companies looking for general contractor or installation contractor in the market

Industry/Entity Type

Wireless Communication

Coding

Coded - Design and coding required

Number of Pages Required

4 page

Font styles to use
Sans Serif

Colors
0555a3
00a990
ffffff

Requirements
Must have
• Wordpress - must be both desktop mobile friendly and mobile is the key -
• should open swiftly on both Android & iOS
• See power point file with presentation about the company; page 5 is our keyservices but other contents can be used too
Nice to have
• panorama pics changing from the height/tower view showing the full overview, could be a slideshow or a short video...
Should not have
• flash animation does not work on iOS so this should be avoided.

```html
<!DOCTYPE html>
<html lang="en">
<head>
<meta charset="utf-8">
<title>Pardune Masts – Service at a Higher Level</title>
<link rel="stylesheet" href="https://fonts.googleapis.com/css2?family=Open+Sans:wght@300;400;600;700&display=swap">
<style>
:root{
  --navy:#2e2785;
  --green:#3d9a36;
  --ink:#222;
  --muted:#666;
  --dark:#2f2f31;
  --footer:#1f1f22;
  --white:#fff;
  --grad:linear-gradient(90deg,var(--navy),var(--green));
}
*{margin:0;padding:0;box-sizing:border-box}
html,body{width:1200px;height:3578px;overflow:hidden}
body{font-family:'Open Sans',sans-serif;color:var(--ink);background:var(--white);position:relative}
.abs{position:absolute}
.btn{position:absolute;display:flex;align-items:center;justify-content:center;color:#fff;background:var(--grad);border-radius:4px;font-size:11px;font-weight:600;text-transform:uppercase;letter-spacing:.3px;z-index:2}
/* top bar */
.topbar{left:0;top:0;width:1200px;height:33px;background:var(--grad);color:#fff;font-size:10px}
.topbar span{position:absolute;top:10px;display:flex;align-items:center;gap:5px}
.social{position:absolute;top:7px;left:934px;display:flex;gap:5px}
.social i{width:18px;height:18px;border-radius:50%;background:#fff;display:block}
/* header */
.header{left:0;top:33px;width:1200px;height:102px;background:#fff}
.logo{position:absolute;left:172px;top:34px;font-size:26px;font-weight:600;color:var(--green);line-height:1}
.nav{position:absolute;left:475px;top:34px;display:flex;align-items:center;font-size:12px;font-weight:600;color:#222}
.nav a{text-decoration:none;color:inherit;margin-right:40px}
.nav a.active{background:var(--navy);color:#fff;padding:9px 12px;border-radius:5px;margin-right:28px}
/* hero */
.hero{left:0;top:135px;width:1200px;height:525px;background:radial-gradient(ellipse at 60% 30%,#b7bcc4 0%,#7c838e 35%,#454b55 75%,#2f333a 100%);color:#fff;text-align:center}
.hero .kicker{position:absolute;top:176px;width:100%;font-size:15px;letter-spacing:12px;font-weight:600}
.hero h1{position:absolute;top:194px;width:100%;font-size:46px;font-weight:400}
.hero h2{position:absolute;top:248px;width:100%;font-size:29px;font-weight:400;letter-spacing:5px}
.dots{position:absolute;display:flex;gap:5px}
.dots i{display:block;width:16px;height:2px;background:rgba(255,255,255,.7)}
.dots i.on{background:#fff}
/* about */
.hex{left:164px;top:694px}
.tower-art{left:1010px;top:715px;width:190px;height:420px;z-index:0;background:linear-gradient(90deg,rgba(240,240,240,0),#ececec 35%,#e4e4e4);}
.about-k{left:572px;top:740px;font-size:15px;color:#333;z-index:2}
.about-h{left:572px;top:760px;font-size:36px;font-weight:600;color:var(--navy);z-index:2}
.about-p{left:575px;top:808px;width:440px;font-size:12px;line-height:19.5px;color:#555;z-index:2}
.about-p p+p{margin-top:19px}
.phone{left:726px;top:1024px;display:flex;align-items:center;gap:10px;font-size:11px;z-index:2}
/* section titles */
.sec-k{width:1200px;text-align:center;font-size:15px;color:#333}
.sec-h{width:1200px;text-align:center;font-size:36px;font-weight:600;color:var(--navy);letter-spacing:.5px}
/* service cards */
.card{width:270px;height:346px;top:1229px;border:1px solid #ccc;background:#fff}
.card .img{height:190px}
.card h3{text-align:center;margin-top:26px;font-size:13px;font-weight:600;color:#222}
.card .bar{width:48px;height:2px;background:var(--navy);margin:10px auto 0}
.card p{text-align:center;font-size:12px;line-height:18px;color:#666;margin:14px 28px 0}
.card .btn{left:77px;bottom:-18px;width:116px;height:36px;border-radius:5px}
/* how we work */
.band-dark{left:0;top:1765px;width:1200px;height:442px;background:var(--dark)}
.work{left:89px;top:1720px;width:503px;height:509px;background:#fff;box-shadow:0 0 20px rgba(0,0,0,.08);text-align:center}
.work h3{margin-top:22px;font-size:22px;font-weight:400;color:#111}
.work .bar{width:48px;height:2px;background:var(--navy);margin:12px auto 0}
.work p{position:absolute;top:384px;left:20px;right:20px;font-size:12px;line-height:20px;color:#666}
/* team */
.member{top:2352px;width:197px;height:336px;border-radius:12px;overflow:hidden;background:var(--navy);color:#fff;text-align:center}
.member .img{height:251px}
.member b{display:block;margin-top:24px;font-size:15px;font-weight:600}
.member span{font-size:12px}
/* cta */
.cta{left:0;top:2741px;width:1200px;height:147px;background:linear-gradient(90deg,#2a2f3a,#1f3850 25%,#2c3140 60%,#383a40)}
.cta p{position:absolute;left:174px;top:58px;color:#fff;font-size:19px;font-weight:400}
.cta .btn{background:#fff;color:#222;left:792px;top:52px;width:133px;height:42px;border-radius:5px}
/* testimonial */
.quote-mark{left:0;top:3012px;width:1200px;text-align:center;font-size:60px;line-height:1;color:#ddd;font-family:Georgia,serif}
.review{left:220px;top:3062px;width:760px;text-align:center;font-size:15.5px;line-height:24px;color:#444}
.avatar{left:522px;top:3172px;width:59px;height:59px;border-radius:50%;background:linear-gradient(135deg,#b58a6a,#4a4d58)}
.who{left:594px;top:3186px;font-size:10.5px;line-height:19px;color:#333}
/* footer */
.footer{left:0;top:3304px;width:1200px;height:233px;background:var(--footer);color:#ddd}
.fcol{position:absolute;top:50px;font-size:10.5px;line-height:22.5px}
.fcol h4{font-size:12px;font-weight:600;color:#fff;margin-bottom:6px;line-height:16px}
.fcol.info{line-height:15.5px}
.fcol.info h4{margin-bottom:14px}
.news-input{position:absolute;left:757px;top:126px;width:263px;height:35px;background:#fff;border-radius:4px;font-size:10px;color:#999;padding:11px 12px}
.news-input .btn{left:186px;top:2px;width:75px;height:31px;font-size:9.5px;border-radius:3px}
.copyright{left:0;top:3537px;width:1200px;height:41px;background:var(--grad);color:#fff;font-size:10.5px;text-align:center;line-height:41px}
</style>
</head>
<body>

<div class="abs topbar">
  <span style="left:172px"><svg width="9" height="11" viewBox="0 0 9 11"><path d="M4.5 0C2 0 0 2 0 4.4 0 7.6 4.5 11 4.5 11S9 7.6 9 4.4C9 2 7 0 4.5 0zm0 6a1.6 1.6 0 110-3.2 1.6 1.6 0 010 3.2z" fill="#fff"/></svg>48 Copperfield Ave, USA</span>
  <span style="left:550px"><svg width="10" height="8" viewBox="0 0 10 8"><rect width="10" height="8" rx="1" fill="#fff"/><path d="M0 1l5 3.5L10 1" stroke="#2e2785" fill="none"/></svg>hello@pardunemasts.com</span>
  <div class="social"><i></i><i></i><i></i><i></i></div>
</div>

<header class="abs header">
  <div class="logo">Pardune Masts</div>
  <nav class="nav">
    <a class="active">HOME</a><a>ABOUT US</a><a>SERVICES</a><a>GALLERY</a><a>CAREERS</a><a>CONTACT</a>
    <svg width="11" height="11" viewBox="0 0 11 11"><circle cx="4.5" cy="4.5" r="3.5" stroke="#222" stroke-width="1.6" fill="none"/><path d="M7 7l3.3 3.3" stroke="#222" stroke-width="1.8"/></svg>
  </nav>
</header>

<section class="abs hero" role="img" aria-label="Lattice telecom tower against a cloudy sky with sun rays">
  <div class="kicker">PARDUNE MASTS</div>
  <h1>Telecommunication Services</h1>
  <h2>SERVICE AT A HIGHER LEVEL</h2>
  <div class="btn" style="left:533px;top:300px;width:135px;height:42px;border-radius:5px">Contact us</div>
  <div class="dots" style="left:571px;top:496px"><i></i><i class="on"></i><i></i></div>
</section>

<svg class="abs hex" width="375" height="410" viewBox="0 0 375 410" role="img" aria-label="Looking up through a lattice tower into a warm sunlit sky">
  <defs><radialGradient id="sky" cx="50%" cy="40%" r="60%"><stop offset="0" stop-color="#f3e2c4"/><stop offset=".6" stop-color="#c9a77e"/><stop offset="1" stop-color="#7c6248"/></radialGradient></defs>
  <path d="M187 14 Q200 4 214 12 L352 98 Q370 110 370 130 L370 286 Q370 306 352 318 L214 402 Q200 410 187 402 L22 318 Q4 306 4 286 L4 130 Q4 110 22 98 Z" fill="var(--navy)"/>
  <path d="M193 2 Q205 -3 217 4 L355 90 Q372 102 372 122 L372 280 Q372 298 355 310 L217 392 Q205 399 193 392 L30 310 Q12 298 12 280 L12 122 Q12 102 30 90 Z" fill="url(#sky)"/>
</svg>
<div class="abs tower-art" role="img" aria-label="Red and white telecom tower with dish antennas"></div>
<div class="abs about-k">ABOUT THE COMPANY</div>
<div class="abs about-h">PARDUNE MASTS</div>
<div class="abs about-p">
  <p>Pardune Masts LLC has been in business since 2014 with combined professional Team experience of over 40 years.<br>Our Team is composed of long-time industry professionals in every aspect of the wireless telecommunications and • commercial construction industries, including project management and site acquisition.</p>
  <p>• Pardune Masts specializes in providing turn-key service by integrating services for the Wireless Telecommunications and Commercial Construction industries, maintaining a footprint throughout the South Eastern, Central and Midwest regions of the United States.</p>
</div>
<div class="btn" style="left:575px;top:1013px;width:133px;height:43px;border-radius:5px">Discover more</div>
<div class="abs phone"><svg width="20" height="20" viewBox="0 0 20 20"><circle cx="10" cy="10" r="9" stroke="var(--green)" stroke-width="1.5" fill="none"/><path d="M6.5 5.5l2 .2.8 2.2-1.2 1a6 6 0 003 3l1-1.2 2.2.8.2 2c-4 1-9-4-8-8z" fill="var(--green)"/></svg>555-014-2290</div>

<div class="abs sec-k" style="top:1150px">OUR SERVICES</div>
<div class="abs sec-h" style="top:1166px">WHATS OUR OFFERS</div>

<div class="abs card" style="left:172px">
  <div class="img" role="img" aria-label="Technician climbing a steel tower" style="background:linear-gradient(135deg,#4b5f86,#8ea3c2 50%,#c8d2de)"></div>
  <h3>WIRELESS TOWER CONSTRUCTION</h3><div class="bar"></div>
  <p>Numquam doloribus impedit at consectetur molestiae tempora ratione possimus in veniam aperiam.</p>
  <div class="btn">Learn more</div>
</div>
<div class="abs card" style="left:465px">
  <div class="img" role="img" aria-label="Black and white antenna towers" style="background:linear-gradient(135deg,#f2f2f2,#9a9a9a 55%,#d6d6d6)"></div>
  <h3>INSTALLATION &amp; MAINTENANCE</h3><div class="bar"></div>
  <p>Numquam doloribus impedit at consectetur molestiae tempora ratione possimus in veniam aperiam.</p>
  <div class="btn">Learn more</div>
</div>
<div class="abs card" style="left:757px">
  <div class="img" role="img" aria-label="Glowing fiber optic cable end" style="background:radial-gradient(circle at 35% 35%,#7fc8f0,#1b4d8a 40%,#061a33)"></div>
  <h3>FIBER &amp; SWEEP TESTING</h3><div class="bar"></div>
  <p>Numquam doloribus impedit at consectetur molestiae tempora ratione possimus in veniam aperiam.</p>
  <div class="btn">Learn more</div>
</div>
<div class="btn" style="left:538px;top:1633px;width:133px;height:44px;border-radius:5px">View all</div>

<div class="abs band-dark"></div>
<div class="abs" style="left:611px;top:1736px;width:500px;height:471px;background:linear-gradient(180deg,#dde4ec,#9fb3c9)" role="img" aria-label="Businessman in glasses holding a laptop"></div>
<div class="abs work">
  <h3>HOW WE WORK</h3><div class="bar"></div>
  <div class="abs" style="left:50px;top:86px;width:400px;height:284px;background:linear-gradient(160deg,#f4f4f4,#d9d9d9)" role="img" aria-label="Isometric diagram of a telecom site with tower, solar panels, batteries, genset and energy management system"></div>
  <p>Numquam doloribus impedit at consectetur molestiae tempora ratione possimus in veniam aperiam, eum consequuntur,</p>
  <div class="btn" style="left:185px;top:437px;width:133px;height:42px;border-radius:5px">Read more</div>
</div>

<div class="abs" style="left:40px;top:2280px;width:115px;height:460px;background:linear-gradient(180deg,rgba(220,200,200,.35),rgba(230,230,230,.1))" role="img" aria-label="Faint telecom tower"></div>
<div class="abs sec-k" style="top:2262px">OUR TEAM</div>
<div class="abs sec-h" style="top:2278px">OUR BEST EXPERTS</div>

<div class="abs member" style="left:172px"><div class="img" role="img" aria-label="Portrait of a technician in glasses" style="background:linear-gradient(180deg,#c9c9c9,#8a8a8a)"></div><b>DORIAN VELLACOTT</b><span>Technician</span></div>
<div class="abs member" style="left:393px"><div class="img" role="img" aria-label="Portrait of a smiling technician in a blue shirt" style="background:linear-gradient(180deg,#e6e6e6,#9fb0c6)"></div><b>MARISOL KEANE</b><span>Technician</span></div>
<div class="abs member" style="left:611px"><div class="img" role="img" aria-label="Portrait of a technician in a dark suit" style="background:linear-gradient(180deg,#d0d0d0,#3a3a3e)"></div><b>TOBIAS ORWELL</b><span>Technician</span></div>
<div class="abs member" style="left:831px"><div class="img" role="img" aria-label="Portrait of a technician in a black suit" style="background:linear-gradient(180deg,#e0e0e0,#2d2d30)"></div><b>ELENA TARVOS</b><span>Technician</span></div>

<section class="abs cta" role="img" aria-label="Network cables and server rack background">
  <p>LOOKING AN ADEQUATE SOLUTION FOR YOUR PROJECT?</p>
  <div class="btn">View all</div>
</section>

<div class="abs sec-k" style="top:2920px">TESTIMONIAL</div>
<div class="abs sec-h" style="top:2940px">CLIENTS’ REVIEWS</div>
<div class="abs quote-mark">“</div>
<div class="abs review">Lorem ipsum dolor sit amet, consectetur adipisicing elit. Iure voluptate numquam culpa natus, maxime eaque totam laudantium vel. Fugit sed dolorem eos dicta quaerat, assumenda dignissimos nemo laborum nisi rem<br>Iure voluptate numquam culpa natus, maxime eaque</div>
<div class="abs avatar" role="img" aria-label="Client portrait"></div>
<div class="abs who">GRETA L. HOLLOWAY<br>New Jersey</div>
<div class="dots" style="left:571px;top:3265px"><i style="background:var(--navy)"></i><i style="background:var(--navy)"></i><i style="background:var(--navy)"></i></div>

<footer class="abs footer">
  <div class="fcol" style="left:171px"><h4>QUICK LINKS</h4>Home<br>About Us<br>Services<br>Gallery<br>Careers<br>Contact</div>
  <div class="fcol" style="left:318px"><h4>USEFUL LINKS</h4>Privacy Policy<br>Terms &amp; Conditions<br>Newsletter<br>Blogs</div>
  <div class="fcol info" style="left:463px"><h4>CONTACT INFO</h4>Dummy text<br>305, Dummy Street P<br>(please add google map) Dummy M55<br><br>Tel: 1-555-014-2290<br><br>Email: hello@pardunemasts.com</div>
  <div class="fcol info" style="left:757px;width:270px"><h4>OUR NEWSLETTER</h4>Wanna stay in touch with the latest news and find out about new products and offers? Subscribe!</div>
  <div class="news-input">Email address here<div class="btn">Subscribe</div></div>
</footer>
<div class="abs copyright">Copyright © 2019 Pardune Masts. All Rights Reserved.</div>

</body>
</html>
```